Banner Ad Design Project for responsive website

Looking to update the main banner on my website www.bridalpathly.com but it will be for our new responsive website, you can see here http://www.bridalpathly.com/dev/
Banner should be 300 px high by1920 pix wide
Please contact me with any questions
Should include:
All the text from the existing banner ie
Bridal Show
THE FIRST 50 BRIDES WILL GET A CHANCE TO WIN $25000
Honeymoon Cruise Giveaway
"Pick the Perfect Gown" casting call
Banner should be 1920 pix wide
Final delivery will require layered psd file and all fonts

Target Market(s)

Brides

Industry/Entity Type

Call

Requirements
Must have
• All the text from the existing banner ie
• Bridal Show
• THE FIRST 50 BRIDES WILL GET A CHANCE TO WIN $25000
• Honeymoon Cruise Giveaway
• "Pick the Perfect Gown" casting call
• Banner should be 1920 pix wide
Nice to have
• The look and feel of our postcard, see attached
Should not have
• Any specifics to any date/time/location as the banner will be online all the time and the specifics for each show will be different

```html
<!DOCTYPE html>
<html lang="en">
<head>
<meta charset="utf-8">
<title>Bridal Show – Honeymoon Cruise Giveaway Banner</title>
<link rel="stylesheet" href="https://fonts.googleapis.com/css2?family=Parisienne&family=Cinzel:wght@400&family=Tinos&display=swap">
<style>
  :root {
    --backdrop: #1c1c1c;
    --brown-light: #5a4a42;
    --brown-dark: #3d302a;
    --paper: #ffffff;
    --paper-edge: #cfcfcf;
    --olive: #8c9d1b;
    --ink: #111111;
    --ornament-light: rgba(255, 255, 255, 0.16);
    --ornament-olive: rgba(140, 157, 27, 0.28);
    --rule-light: rgba(255, 255, 255, 0.75);
  }
  * { margin: 0; padding: 0; box-sizing: border-box; }
  html, body { width: 1200px; height: 900px; overflow: hidden; background: var(--backdrop); }
  .canvas { position: relative; width: 1200px; height: 900px; overflow: hidden; }

  /* Banner built at its delivery size (1920 × 300) and scaled to fit the canvas width */
  .banner {
    position: absolute; left: 0; top: 356px;
    width: 1920px; height: 300px;
    transform: scale(0.625); transform-origin: top left;
    overflow: hidden;
    box-shadow: 0 0 18px rgba(0,0,0,0.6);
  }
  .banner-shapes { position: absolute; inset: 0; }

  .headline {
    position: absolute; left: 40px; width: 560px; top: 92px;
    text-align: center;
    font-family: "Parisienne", cursive;
    font-size: 96px; line-height: 1; font-weight: 400;
    color: var(--olive);
  }

  .offer {
    position: absolute; left: 760px; width: 1100px; top: 30px;
    display: flex; flex-direction: column; align-items: center;
  }
  .offer-row { display: flex; align-items: center; gap: 16px; }
  .offer-lead {
    text-align: right;
    font-family: "Cinzel", serif;
    font-size: 30px; line-height: 38px; color: var(--ink);
  }
  .offer-amount {
    font-family: "Tinos", serif;
    font-size: 60px; line-height: 1; color: var(--ink);
  }
  .giveaway {
    margin-top: 6px;
    font-family: "Parisienne", cursive;
    font-size: 72px; line-height: 84px; font-weight: 400; color: var(--ink);
  }
  .casting-call {
    align-self: flex-end; margin-right: 40px;
    font-family: "Parisienne", cursive;
    font-size: 48px; line-height: 56px; color: var(--olive);
  }
</style>
</head>
<body>
<div class="canvas">
  <section class="banner">
    <svg class="banner-shapes" width="1920" height="300" viewBox="0 0 1920 300">
      <defs>
        <linearGradient id="header-tone" x1="0" y1="0" x2="1" y2="1">
          <stop offset="0" stop-color="var(--brown-light)"/>
          <stop offset="1" stop-color="var(--brown-dark)"/>
        </linearGradient>
        <radialGradient id="paper-tone" cx="0.5" cy="0.45" r="0.65">
          <stop offset="0.5" stop-color="var(--paper)"/>
          <stop offset="1" stop-color="var(--paper-edge)"/>
        </radialGradient>
      </defs>
      <rect class="header-field" width="1920" height="300" fill="url(#header-tone)"/>
      <rect class="leaf-pattern" width="700" height="300" fill="rgba(255,255,255,0.03)" role="img" aria-label="Faint scattered leaf pattern across the brown field"/>
      <path class="paper-panel" d="M820 0 C640 80 640 220 820 300 L1920 300 L1920 0 Z" fill="url(#paper-tone)"/>
      <line class="header-rule" x1="190" y1="88" x2="450" y2="88" stroke="var(--rule-light)" stroke-width="1.5"/>
      <line class="header-rule" x1="120" y1="202" x2="520" y2="202" stroke="var(--rule-light)" stroke-width="1.5"/>
      <rect class="flourish-top" x="225" y="34" width="190" height="46" rx="20" fill="var(--ornament-light)" role="img" aria-label="Calligraphic flourish above the title"/>
      <rect class="flourish-bottom" x="210" y="208" width="220" height="66" rx="28" fill="var(--ornament-light)" role="img" aria-label="Calligraphic flourish below the title"/>
      <line class="side-rule" x1="735" y1="100" x2="735" y2="200" stroke="var(--olive)" stroke-width="2"/>
      <line class="side-rule" x1="1890" y1="24" x2="1890" y2="276" stroke="var(--olive)" stroke-width="2"/>
      <rect class="flourish-footer" x="1230" y="266" width="120" height="26" rx="12" fill="var(--ornament-olive)" role="img" aria-label="Small olive flourish with two birds"/>
    </svg>

    <h1 class="headline">Bridal Show</h1>

    <div class="offer">
      <div class="offer-row">
        <p class="offer-lead">THE FIRST 50 BRIDES WILL<br>GET A CHANCE TO WIN</p>
        <p class="offer-amount">$25000</p>
      </div>
      <h2 class="giveaway">Honeymoon Cruise Giveaway</h2>
      <p class="casting-call">Pick the Perfect Gown Casting Call</p>
    </div>
  </section>
</div>
</body>
</html>
```